Business Card Design Project

I help solve problems that people have with real estate, so I buy homes for cash that they no longer want, can't afford, inherited, etc. and fix and sell them or rent them or take over mortgage payments. See website: www.quickhomepurchase-example.com

Industry/Entity Type

Real Estate

Contact Information for Business Card

Not exactly sure. Looking for a design that either is similar to the website www.quickhomepurchase-example.com or that reflects what I do as described below. If it can look a little luxurious to show I can buy the houses for cash and I fix them and sell them, it's a bonus. I seem to like some of the higher end things like foil or black or something that makes it stand out.

Font styles to use
Serif

Requirements
Nice to have
• I seem to like black or clear. I like things to stand out and be different.

```html
<!DOCTYPE html>
<html lang="en">
<head>
<meta charset="utf-8">
<title>Renewal Homestead — Business Cards</title>
<link href="https://fonts.googleapis.com/css2?family=Montserrat:wght@400;700;800&display=swap" rel="stylesheet">
<style>
  :root {
    --bg: #d9d9d9;
    --card: #ffffff;
    --green-deep: #1f5a2c;
    --green-mid: #2a7a34;
    --green-bright: #22b024;
    --navy: #1c2452;
    --teal: #2aa7c4;
    --text: #1c2452;
  }
  * { box-sizing: border-box; margin: 0; padding: 0; }
  html, body { width: 1200px; height: 750px; overflow: hidden; }
  body {
    background: var(--bg);
    font-family: "Montserrat", sans-serif;
    position: relative;
  }
  .card {
    position: absolute;
    width: 525px;
    height: 300px;
    background: var(--card);
    border-radius: 28px;
    overflow: hidden;
    box-shadow: 0 10px 24px rgba(0,0,0,0.18);
  }
  .card--contact { left: 50px; top: 225px; }
  .card--brand { left: 625px; top: 225px; }
  .card__wave { position: absolute; inset: 0; width: 100%; height: 100%; }

  .holder { position: absolute; left: 150px; top: 92px; }
  .holder__name {
    font-weight: 800; font-size: 24px; letter-spacing: 1px; color: var(--navy); line-height: 1.1;
  }
  .holder__role {
    font-weight: 400; font-size: 15px; letter-spacing: 4px; color: var(--teal); line-height: 1.2;
  }

  .company-mark {
    position: absolute; right: 30px; top: 30px;
    display: flex; align-items: center; gap: 6px;
    font-weight: 700; font-size: 13px; color: var(--green-deep);
  }
  .company-mark__dot {
    width: 12px; height: 12px; border-radius: 50%; background: var(--green-deep);
  }

  .contact-list {
    position: absolute; right: 30px; top: 74px;
    list-style: none;
  }
  .contact-list__item {
    display: flex; align-items: center; justify-content: flex-end; gap: 10px;
    font-size: 11px; color: var(--text); height: 26px; text-align: right; line-height: 1.2;
  }
  .contact-list__icon { width: 20px; height: 20px; flex: none; }

  .brand-name {
    position: absolute; right: 40px; top: 78px;
    text-align: right;
    font-weight: 800; font-size: 44px; line-height: 1.05; letter-spacing: 1px;
    color: var(--green-mid);
  }
</style>
</head>
<body>

<section class="card card--contact" aria-label="Contact side">
  <svg class="card__wave" viewBox="0 0 525 300" preserveAspectRatio="none" aria-hidden="true">
    <defs>
      <linearGradient id="brightA" x1="0" y1="0" x2="1" y2="1">
        <stop offset="0" stop-color="#1c8c22"/><stop offset="1" stop-color="#2cc42a"/>
      </linearGradient>
    </defs>
    <path d="M0,300 L0,125 C30,104 70,98 95,108 C130,185 200,220 300,228 C350,232 385,262 400,300 Z" fill="url(#brightA)"/>
    <path d="M0,300 L0,142 C28,124 58,118 78,124 C115,200 180,238 280,246 C320,250 345,275 355,300 Z" fill="var(--green-deep)"/>
  </svg>

  <div class="holder">
    <p class="holder__name">YOUR NAME</p>
    <p class="holder__role">your position</p>
  </div>

  <div class="company-mark"><span>Renewal Homestead</span><span class="company-mark__dot"></span></div>

  <ul class="contact-list">
    <li class="contact-list__item">
      <span>000 Street Name,<br>City Name, 00000 - ST</span>
      <svg class="contact-list__icon" viewBox="0 0 20 20" aria-hidden="true"><circle cx="10" cy="10" r="10" fill="var(--green-deep)"/><path d="M10 4.5a3.5 3.5 0 0 0-3.5 3.5c0 2.6 3.5 6.5 3.5 6.5s3.5-3.9 3.5-6.5A3.5 3.5 0 0 0 10 4.5z" fill="#fff"/><circle cx="10" cy="8" r="1.3" fill="var(--green-deep)"/></svg>
    </li>
    <li class="contact-list__item">
      <span>companywebsite.com</span>
      <svg class="contact-list__icon" viewBox="0 0 20 20" aria-hidden="true"><circle cx="10" cy="10" r="10" fill="var(--green-deep)"/><g fill="none" stroke="#fff" stroke-width="1.1"><circle cx="10" cy="10" r="5"/><ellipse cx="10" cy="10" rx="2.2" ry="5"/><path d="M5 10h10"/></g></svg>
    </li>
    <li class="contact-list__item">
      <span>youremail@company.com</span>
      <svg class="contact-list__icon" viewBox="0 0 20 20" aria-hidden="true"><circle cx="10" cy="10" r="10" fill="var(--green-deep)"/><rect x="5" y="6.5" width="10" height="7" fill="#fff"/><path d="M5 6.5l5 4 5-4" fill="none" stroke="var(--green-deep)" stroke-width="1"/></svg>
    </li>
    <li class="contact-list__item">
      <span>+ 0 000 . 0000</span>
      <svg class="contact-list__icon" viewBox="0 0 20 20" aria-hidden="true"><circle cx="10" cy="10" r="10" fill="var(--green-deep)"/><path d="M7 5.5l1.8 2.3-1 1.3c.6 1.3 1.6 2.3 2.9 2.9l1.3-1 2.3 1.8-1 1.7c-3.5-.2-6.9-3.6-7.1-7.1z" fill="#fff"/></svg>
    </li>
  </ul>
</section>

<section class="card card--brand" aria-label="Brand side">
  <svg class="card__wave" viewBox="0 0 525 300" preserveAspectRatio="none" aria-hidden="true">
    <defs>
      <linearGradient id="brightB" x1="0" y1="0" x2="1" y2="1">
        <stop offset="0" stop-color="#1c8c22"/><stop offset="1" stop-color="#2cc42a"/>
      </linearGradient>
    </defs>
    <path d="M0,300 L0,125 C30,104 70,98 95,108 C130,185 200,220 300,228 C350,232 385,262 400,300 Z" fill="url(#brightB)"/>
    <path d="M0,300 L0,142 C28,124 58,118 78,124 C115,200 180,238 280,246 C320,250 345,275 355,300 Z" fill="var(--green-deep)"/>
  </svg>

  <h1 class="brand-name">RENEWAL<br>HOMESTEAD</h1>
</section>

</body>
</html>
```